Trade Show:
- Need as a backdrop visual
- Size: 8' x 10' - Template attached with panels
- Theme of the show is vacation and the main visual is to have a plane landing. Have the plane be Tidy Nook branded with logo and the tagline "Make Ready Made Easy".
- Have the visual be animated and fun! With the plane landing have the visual be in a daytime setting with a 'Charlotte skyline' in the background if it works in the design.

See animated designs to get an idea.

Text needed on the backdrop:
- "Take your seat on this turn transformation flight..."
- "...and get ready for a smooth landing on your next turn!"
Separate the two sets of text within the design.

Font styles to use
Sans Serif
Other font styles liked:
• Covered by your Grace - Regular

Requirements
Must have
• plane with Tidy Nook logo or branded colors

```html
<!DOCTYPE html>
<html lang="en">
<head>
<meta charset="utf-8">
<title>Tidy Nook Trade Show Backdrop</title>
<link rel="stylesheet" href="https://fonts.googleapis.com/css2?family=Bungee&family=Bungee+Shade&family=PT+Sans+Narrow&display=swap">
<style>
  :root {
    --template-bg: #d9e9f3;
    --side-band: #93b5c9;
    --stitch-red: #e8392b;
    --dimension-blue: #2c4fa3;
    --guide-green: #3f9a3a;
    --guide-black: #222;
    --sky-top: #b6dcf3;
    --sky-mid: #b3bde2;
    --sky-low: #d9cbe6;
    --sky-bottom: #f6e2ee;
    --headline-light: #7f7fc0;
    --headline-dark: #4b2a72;
    --brand-navy: #17132f;
  }
  * { margin: 0; padding: 0; box-sizing: border-box; }
  html, body { width: 1200px; height: 750px; overflow: hidden; background: var(--template-bg); }
  .backdrop-template { position: relative; width: 1200px; height: 750px; background: var(--template-bg); }
  .side-band { position: absolute; top: 0; width: 109px; height: 750px; background: var(--side-band); }
  .side-band--left { left: 0; }
  .side-band--right { left: 1091px; }
  .sky-strip, .sky-panel {
    position: absolute;
    background: linear-gradient(180deg, var(--sky-top) 0%, #c9e4f5 35%, var(--sky-mid) 58%, var(--sky-low) 80%, var(--sky-bottom) 100%);
  }
  .sky-strip--left { left: 36px; top: 57px; width: 59px; height: 634px; background: linear-gradient(180deg, #e3eff9 0%, #dbe9f6 45%, #ecdde8 75%, #fbe8f0 100%); }
  .sky-strip--right { left: 1106px; top: 58px; width: 59px; height: 633px; background: linear-gradient(180deg, #9dc2e8 0%, #b4cdee 40%, #c3c3e6 70%, #f1dbe9 100%); }
  .sky-panel { left: 165px; top: 58px; width: 871px; height: 633px; }
  .plane-art {
    position: absolute; left: 320px; top: 323px; width: 222px; height: 121px;
    background: radial-gradient(ellipse at center, rgba(255,255,255,0.95) 0%, rgba(255,255,255,0.7) 55%, rgba(255,255,255,0) 75%);
  }
  .brand-name {
    position: absolute; left: 222px; top: 582px;
    font-family: "Bungee", sans-serif; font-size: 34px; line-height: 36px;
    color: var(--brand-navy); display: flex; align-items: center; gap: 10px;
  }
  .brand-name__mark { width: 16px; height: 16px; background: var(--brand-navy); }
  .guides { position: absolute; inset: 0; }
  .headline { font-family: "Bungee Shade", sans-serif; }
  .headline--top { fill: var(--headline-light); }
  .headline--bottom { fill: var(--headline-dark); }
  .stitch-label { font-family: "PT Sans Narrow", sans-serif; font-size: 15px; fill: var(--stitch-red); }
  .dimension-label { font-family: "PT Sans Narrow", sans-serif; font-size: 22px; fill: var(--guide-green); }
</style>
</head>
<body>
<main class="backdrop-template">
  <div class="side-band side-band--left"></div>
  <div class="side-band side-band--right"></div>
  <div class="sky-strip sky-strip--left" role="img" aria-label="Soft daytime sky with clouds, side panel"></div>
  <div class="sky-strip sky-strip--right" role="img" aria-label="Soft daytime sky with clouds, side panel"></div>
  <div class="sky-panel" role="img" aria-label="Daytime sky with soft pastel clouds"></div>
  <div class="plane-art" role="img" aria-label="White branded passenger jet descending for landing"></div>

  <div class="brand-name"><span>Tidy<br>Nook</span><span class="brand-name__mark"></span></div>

  <svg class="guides" width="1200" height="750" viewBox="0 0 1200 750">
    <g class="headlines">
      <text class="headline headline--top" x="223" y="146" font-size="36" textLength="558" lengthAdjust="spacingAndGlyphs">TAKE YOUR SEAT ON THIS</text>
      <text class="headline headline--top" x="225" y="198" font-size="36" textLength="762" lengthAdjust="spacingAndGlyphs">TURN TRANSFORMATION FLIGHT...</text>
      <text class="headline headline--bottom" x="464" y="499" font-size="38" textLength="544" lengthAdjust="spacingAndGlyphs">... AND GET READY FOR A</text>
      <text class="headline headline--bottom" x="458" y="573" font-size="54" textLength="550" lengthAdjust="spacingAndGlyphs">SMOOTH LANDING</text>
      <text class="headline headline--bottom" x="546" y="640" font-size="40" textLength="462" lengthAdjust="spacingAndGlyphs">ON YOUR NEXT TURN!</text>
    </g>

    <g class="stitch-lines" fill="none" stroke="var(--stitch-red)" stroke-width="1" stroke-dasharray="3 3">
      <rect x="2.5" y="2.5" width="1195" height="745"/>
      <line x1="0" y1="18" x2="1200" y2="18"/>
      <line x1="0" y1="729" x2="1200" y2="729"/>
      <line x1="19" y1="0" x2="19" y2="750"/>
      <line x1="1182" y1="0" x2="1182" y2="750"/>
    </g>
    <g class="stitch-labels">
      <rect x="555" y="3" width="100" height="14" fill="var(--template-bg)"/>
      <text class="stitch-label" x="605" y="16" text-anchor="middle">2 stitching lines</text>
      <rect x="555" y="731" width="100" height="14" fill="var(--template-bg)"/>
      <text class="stitch-label" x="605" y="743" text-anchor="middle">2 stitching lines</text>
      <text class="stitch-label" transform="translate(14 375) rotate(-90)" text-anchor="middle">2 stitching lines</text>
      <text class="stitch-label" transform="translate(1193 375) rotate(-90)" text-anchor="middle">2 stitching lines</text>
    </g>

    <g class="dimension-height" fill="none" stroke="var(--dimension-blue)" stroke-width="1">
      <line x1="130" y1="5" x2="130" y2="745"/>
      <polyline points="114,15 130,5 146,15"/>
      <polyline points="114,735 130,745 146,735"/>
    </g>
    <text class="dimension-label" x="131" y="384">90”</text>

    <g class="panel-width-guides" fill="none" stroke="var(--guide-green)" stroke-width="0.8">
      <line x1="112" y1="150" x2="165" y2="150"/>
      <polyline points="128,135 112,150 128,163"/>
      <line x1="1036" y1="150" x2="1086" y2="150"/>
      <polyline points="1070,135 1086,150 1070,163"/>
    </g>
    <g class="full-width-guides" fill="none" stroke="var(--guide-black)" stroke-width="0.7">
      <line x1="5" y1="670" x2="165" y2="670"/>
      <polyline points="19,654 5,670 19,683"/>
      <line x1="1036" y1="670" x2="1195" y2="670"/>
      <polyline points="1181,654 1195,670 1181,683"/>
    </g>
  </svg>
</main>
</body>
</html>
```